ARRIVAL OF MARTIN THE OLD COUSIN

Hello everyone !

Our establishment, on 57 in CAMBRAI will have the pleasure of welcoming MARTIN LE VIEUX COUSIN, idol of young people, on Friday May 13, 2022, from 7:00 p.m.
On the program, photo session and dedications.
A VIP table will be offered to share the meal with him!
Only 12 places available at his table!
The brasserie will offer a barbecue for the occasion.
Admission with meal: €15
Seating at the VIP table: €65 (starter - main course - dessert); Champagne.
Happy HOURS on beers and cocktails!
Reservation strongly recommended.

I remain at your disposal ;

To your ideas!

```html
<!DOCTYPE html>
<html lang="en">
<head>
<meta charset="utf-8">
<title>Martin Le Vieux Cousin at Taverne du Beffroi</title>
<link rel="stylesheet" href="https://fonts.googleapis.com/css2?family=Playfair+Display:ital,wght@1,700;1,800&family=Montserrat:wght@800&family=Poppins:ital,wght@0,300;0,400;0,500;1,600&display=swap">
<style>
:root{
  --gold:#c8922e;
  --yellow:#fdd23a;
  --black:#050505;
  --charcoal:#2b2b2b;
  --white:#ffffff;
  --ink:#1b1b1b;
  --paper:#f2f2f2;
}
*{margin:0;padding:0;box-sizing:border-box}
html,body{width:848px;height:1200px;overflow:hidden;background:var(--charcoal)}
.poster{position:relative;width:848px;height:1200px;overflow:hidden;background:var(--charcoal);font-family:'Poppins',sans-serif;color:var(--white)}
.header{position:absolute;left:0;top:0;width:848px;height:190px;background:linear-gradient(180deg,#ffffff 0%,var(--paper) 100%)}
.sun{position:absolute;left:715px;top:140px;width:330px;height:330px;border-radius:50%;background:var(--yellow)}
.venue-name{position:absolute;left:0;top:76px;width:848px;text-align:center;font-family:'Poppins',sans-serif;font-weight:500;font-size:40px;letter-spacing:2px;color:var(--gold);line-height:1}
.stage{position:absolute;left:0;top:180px;width:848px;height:386px;background:var(--black);border-top-right-radius:190px 220px}
.intro{position:absolute;left:68px;top:220px;font-family:'Poppins',sans-serif;font-style:italic;font-weight:600;font-size:19.5px;line-height:36px;color:var(--yellow)}
.guest{position:absolute;left:66px;top:336px;font-family:'Playfair Display',serif;font-style:italic;font-weight:800;font-size:72px;line-height:90px;color:var(--white)}
.ribbon{position:absolute;left:543px;top:300px;width:263px;height:755px;background:var(--yellow)}
.portrait{position:absolute;left:520px;top:208px;width:298px;height:298px;border-radius:50%;background:var(--black);border:2px solid var(--yellow);padding:7px}
.portrait-fill{width:100%;height:100%;border-radius:50%;background:radial-gradient(circle at 55% 35%,#8a8a8a 0%,#3a3a3a 45%,#141414 100%)}
.camera{position:absolute;left:563px;top:563px;width:216px;height:345px;border-radius:12px;background:linear-gradient(180deg,#ffffff 0%,#e9e9e9 100%)}
.program{position:absolute;left:543px;top:948px;width:263px;text-align:center;font-family:'Playfair Display',serif;font-style:italic;font-weight:700;font-size:22px;line-height:28px;color:var(--ink)}
.rule{position:absolute;left:53px;width:450px;height:1px;background:var(--yellow)}
.date{position:absolute;left:40px;top:574px;width:476px;text-align:center;font-family:'Montserrat',sans-serif;font-weight:800;font-size:54px;letter-spacing:5px;color:var(--yellow);line-height:64px}
.time{position:absolute;left:40px;top:641px;width:476px;text-align:center;font-weight:300;font-size:28px;letter-spacing:4.5px;color:var(--white)}
.details{position:absolute;left:60px;top:719px;width:460px;list-style:none;display:grid;grid-template-columns:227px 227px;grid-template-rows:95px 109px auto}
.detail{display:flex;gap:12px;font-size:14.5px;line-height:19.5px;font-weight:400}
.detail span{max-width:165px}
.detail svg{flex:none;width:28px;height:28px;margin-top:-3px}
.reservation{position:absolute;left:52px;top:1010px;width:456px;height:44px;background:var(--yellow);color:var(--ink);font-family:'Playfair Display',serif;font-style:italic;font-weight:700;font-size:24.5px;text-align:center;line-height:44px}
.footer{position:absolute;left:0;top:1093px;width:848px;height:78px;background:var(--black);border-top:2px solid var(--yellow);border-bottom:2px solid var(--yellow);display:flex;align-items:center;justify-content:center;font-weight:500;font-size:28px;color:var(--white);gap:14px}
</style>
</head>
<body>
<main class="poster">
  <header class="header">
    <p class="venue-name">TAVERNE DU BEFFROI</p>
  </header>
  <div class="sun"></div>
  <section class="stage"></section>
  <div class="ribbon"></div>
  <p class="intro">Our Establishment, On 57 in Cambrai<br>Will Have The Pleasure Of Welcoming</p>
  <h1 class="guest">Martin Le<br>Vieux Cousin</h1>
  <div class="portrait"><div class="portrait-fill" role="img" aria-label="Portrait of Martin Le Vieux Cousin in a black leather jacket, arms crossed"></div></div>
  <div class="rule" style="top:565px"></div>
  <p class="date">MAY 13, 2022</p>
  <p class="time">FRIDAY | FROM 7:00 P.M.</p>
  <div class="rule" style="top:688px"></div>
  <ul class="details">
    <li class="detail"><svg viewBox="0 0 24 24"><path fill="#fdd23a" d="M12 1.5l3.1 7 7.6.7-5.8 5 1.8 7.5L12 17.8l-6.7 3.9 1.8-7.5-5.8-5 7.6-.7z"/></svg><span>A VIP table will be offered to share the meal with him!</span></li>
    <li class="detail"><svg viewBox="0 0 24 24"><path fill="#fdd23a" d="M12 1.5l3.1 7 7.6.7-5.8 5 1.8 7.5L12 17.8l-6.7 3.9 1.8-7.5-5.8-5 7.6-.7z"/></svg><span>Only 12 places<br>available<br>at his table!</span></li>
    <li class="detail"><svg viewBox="0 0 24 24"><path fill="#fdd23a" d="M12 1.5l3.1 7 7.6.7-5.8 5 1.8 7.5L12 17.8l-6.7 3.9 1.8-7.5-5.8-5 7.6-.7z"/></svg><span>Admission with<br>meal: €15</span></li>
    <li class="detail"><svg viewBox="0 0 24 24"><path fill="#fdd23a" d="M12 1.5l3.1 7 7.6.7-5.8 5 1.8 7.5L12 17.8l-6.7 3.9 1.8-7.5-5.8-5 7.6-.7z"/></svg><span>Seating at the VIP table: €65 (starter - main course - dessert); Champagne.</span></li>
    <li class="detail"><svg viewBox="0 0 24 24"><path fill="#fdd23a" d="M12 1.5l3.1 7 7.6.7-5.8 5 1.8 7.5L12 17.8l-6.7 3.9 1.8-7.5-5.8-5 7.6-.7z"/></svg><span>The brasserie will offer a barbecue for the occasion.</span></li>
    <li class="detail"><svg viewBox="0 0 24 24"><path fill="#fdd23a" d="M12 1.5l3.1 7 7.6.7-5.8 5 1.8 7.5L12 17.8l-6.7 3.9 1.8-7.5-5.8-5 7.6-.7z"/></svg><span>Happy HOURS<br>on beers<br>and cocktails!</span></li>
  </ul>
  <p class="reservation">Reservation strongly recommended</p>
  <div class="camera" role="img" aria-label="Photo of a camera mounted on a tripod"></div>
  <p class="program">On the program,<br>photo session and<br>dedications</p>
  <footer class="footer"><span>013 579 2468</span><span>|</span><span>contact@tavernedubeffroi.fr</span></footer>
</main>
</body>
</html>
```